Bright Path Attorneys Billboard Design for Personal Injury Law Firm

Need a billboard design that we can use for different versions. 1400px X 400px jpeg or png
I have attached the logo and the attorney for the billboard. Attorney Marla Benning
Here is a link to our current website brightpathlegalgroup.example

HEADLINE: HIT BY A TRUCK?
SUBHEAD: NO FEE. BIG FIGHT.
877-GRANTLY

HEADLINE: ACCIDENT?
SUBHEAD: NO FEE, UNLESS WE WIN!
877-GRANTLY

HEADLINE: BIG TRUCK. BIG CASE.
SUBHEAD: YOU PAY $0 UPFRONT
877-GRANTLY

Target Market(s)

People in Car Accident

Industry/Entity Type

Personal Injury Attorneys

```html
<!DOCTYPE html>
<html lang="en">
<head>
<meta charset="utf-8">
<title>Bright Path Attorneys – Truck Billboard</title>
<link rel="stylesheet" href="https://fonts.googleapis.com/css2?family=Oswald:wght@500;600;700&family=Montserrat:wght@600&display=swap">
<style>
  :root {
    --page-bg: #e9ebef;
    --board-bg: #050505;
    --headline-start: #c9cbe6;
    --headline-end: #ffffff;
    --text-white: #ffffff;
    --phone-yellow: #fff200;
    --pill-line: #5a5a5a;
    --brand-green: #6cc04a;
    --truck-dark: #141414;
    --truck-mid: #2e2e2e;
  }
  * { box-sizing: border-box; margin: 0; padding: 0; }
  html, body {
    width: 1200px;
    height: 840px;
    overflow: hidden;
    background: var(--page-bg);
  }
  .billboard {
    position: absolute;
    left: 40px;
    top: 260px;
    width: 1120px;
    height: 320px;
    background: var(--board-bg);
    overflow: hidden;
  }
  .headline {
    position: absolute;
    left: 36px;
    top: 22px;
    font-family: "Oswald", sans-serif;
    font-weight: 700;
    font-size: 104px;
    line-height: 1;
    letter-spacing: 1px;
    background: linear-gradient(90deg, var(--headline-start) 0%, var(--headline-start) 45%, var(--headline-end) 80%);
    -webkit-background-clip: text;
    background-clip: text;
    color: transparent;
    white-space: nowrap;
  }
  .subhead {
    position: absolute;
    left: 36px;
    top: 128px;
    font-family: "Oswald", sans-serif;
    font-weight: 700;
    font-size: 80px;
    line-height: 1;
    color: var(--text-white);
    white-space: nowrap;
  }
  .contact-pill {
    position: absolute;
    left: 32px;
    top: 226px;
    width: 690px;
    height: 80px;
    border: 1.5px solid var(--pill-line);
    border-radius: 16px;
    display: flex;
    align-items: center;
    padding: 0 18px;
  }
  .phone {
    font-family: "Oswald", sans-serif;
    font-weight: 600;
    font-size: 60px;
    letter-spacing: 5px;
    color: var(--phone-yellow);
    line-height: 1;
    white-space: nowrap;
  }
  .divider {
    width: 1.5px;
    height: 54px;
    background: var(--pill-line);
    margin: 0 18px;
  }
  .brand {
    display: flex;
    align-items: center;
    gap: 10px;
  }
  .brand-dot {
    width: 18px;
    height: 18px;
    border-radius: 50%;
    background: var(--brand-green);
    flex: none;
  }
  .brand-name {
    font-family: "Oswald", sans-serif;
    font-weight: 500;
    font-size: 22px;
    line-height: 1.05;
    color: var(--text-white);
    text-transform: uppercase;
  }
  .truck-photo {
    position: absolute;
    right: 0;
    top: 0;
    width: 350px;
    height: 320px;
    background: radial-gradient(ellipse at 55% 55%, var(--truck-mid) 0%, var(--truck-dark) 55%, var(--board-bg) 100%);
  }
</style>
</head>
<body>
  <div class="billboard">
    <h1 class="headline">HIT BY A TRUCK?</h1>
    <p class="subhead">NO FEE. BIG FIGHT.</p>
    <div class="contact-pill">
      <span class="phone">877-GRANTLY</span>
      <span class="divider"></span>
      <div class="brand">
        <span class="brand-dot"></span>
        <span class="brand-name">Bright Path<br>Attorneys</span>
      </div>
    </div>
    <div class="truck-photo" role="img" aria-label="Photo of a black semi truck cab with chrome grille, seen from the front"></div>
  </div>
</body>
</html>
```